Business Card Design Project

Basketball Training program

Offers: Travel Club Program - Camps - Clinics - Private Training

website: rivetbasketball.example
Phone Contact: Main Phone: 555-317-4826
Email: rivet.basketball@mailbox.example

Industry/Entity Type

Business

Contact Information for Business Card

Need one for the following coaches:
Marlo Quintrell - Boys & Girls Basketball Coach
Noweni Tasker - Girls Basketball Coach
Anselmo Duvray - Director/Head Coach
Hollis Ruk- Boys Basketball
Warren Olivash - Boys Basketball
Tomas Ferlanga - Boys Basketball
Kavin Sotherby- Boys Basketball/ Trainer
Al Varnock - Boys & Girls Basketball Coach

Basketball Training program Logo - one side

Logo on the corner
new one on the left (RB)
old one on the right (old one is with the rivet and basketball)

```html
<!DOCTYPE html>
<html lang="en">
<head>
<meta charset="utf-8">
<title>Rivet Basketball – Business Card</title>
<link rel="stylesheet" href="https://fonts.googleapis.com/css2?family=Arimo:wght@400;700&family=Tinos:wght@400;700&display=swap">
<style>
  :root {
    --page: #e6e4e0;
    --paper: #ffffff;
    --paper-shade: #ececec;
    --ink: #2b2b2b;
    --black: #0b0b0b;
    --gold: #f1b300;
    --grey-line: #9a9a9a;
    --faint: #ebebeb;
    --white: #ffffff;
  }
  * { box-sizing: border-box; margin: 0; padding: 0; }
  html, body { width: 1200px; height: 902px; overflow: hidden; background: var(--page); }
  .canvas { position: relative; width: 1200px; height: 902px; }
  .card {
    position: absolute; left: 240px; width: 720px; height: 414px;
    background: linear-gradient(180deg, var(--paper) 0%, var(--paper-shade) 100%);
    box-shadow: 0 6px 18px rgba(0,0,0,.18);
    overflow: hidden;
  }
  .card--back { top: 26px; }
  .card--front { top: 462px; }

  /* back side */
  .services { position: absolute; top: 62px; left: 0; width: 720px; height: 110px; font-family: "Arimo", sans-serif; font-size: 26px; color: var(--ink); }
  .services__col { position: absolute; top: 0; display: flex; flex-direction: column; gap: 10px; }
  .services__col--left { right: 372px; align-items: flex-end; }
  .services__col--right { left: 372px; align-items: flex-start; }
  .service { display: flex; align-items: center; gap: 12px; line-height: 32px; }
  .service svg { width: 14px; height: 14px; }
  .services__divider { position: absolute; left: 359px; top: -6px; width: 2px; height: 100px; background: var(--gold); }

  .band-back { position: absolute; left: 0; top: 258px; width: 720px; height: 78px; background: var(--black); }
  .band-back__rule { position: absolute; left: 0; width: 720px; height: 3px; background: var(--grey-line); }
  .band-back__rule--top { top: 248px; }
  .band-back__rule--bottom { top: 344px; }
  .brand { position: absolute; left: 56px; top: 238px; display: flex; align-items: center; gap: 18px; }
  .brand__dot { width: 118px; height: 118px; border-radius: 50%; background: var(--gold); }
  .brand__name { font-family: "Arimo", sans-serif; font-weight: 700; font-size: 52px; color: var(--white); letter-spacing: 2px; }

  /* front side */
  .backdrop-circle { position: absolute; left: 230px; top: -60px; width: 300px; height: 300px; border-radius: 50%; background: var(--faint); }
  .headline { position: absolute; left: 0; top: 130px; width: 720px; text-align: center; font-family: "Tinos", serif; font-weight: 400; font-size: 50px; line-height: 60px; color: var(--gold); }
  .stripe { position: absolute; left: 0; top: 232px; width: 720px; height: 26px; background: var(--gold); border-top: 3px solid var(--grey-line); border-bottom: 3px solid var(--grey-line); }
  .band-front { position: absolute; left: 0; top: 258px; width: 720px; height: 156px; background: var(--black); }
  .person { position: absolute; left: 36px; top: 300px; color: var(--white); }
  .person__name { font-family: "Tinos", serif; font-size: 38px; line-height: 44px; }
  .person__role { font-family: "Arimo", sans-serif; font-size: 21px; margin-top: 4px; }
  .contact-divider { position: absolute; left: 398px; top: 282px; width: 2px; height: 110px; background: var(--white); }
  .contacts { position: absolute; left: 414px; top: 288px; list-style: none; font-family: "Arimo", sans-serif; font-size: 17px; color: var(--white); display: flex; flex-direction: column; gap: 12px; }
  .contacts li { display: flex; align-items: center; gap: 10px; }
  .contacts svg { width: 18px; height: 18px; flex: none; }
</style>
</head>
<body>
<main class="canvas">

  <section class="card card--back" aria-label="Card back">
    <div class="services">
      <div class="services__col services__col--left">
        <span class="service">Camps <svg viewBox="0 0 14 14"><circle cx="7" cy="7" r="6" fill="none" stroke="#777" stroke-width="1.5"/><circle cx="7" cy="7" r="2.5" fill="#777"/></svg></span>
        <span class="service">Travel Club Program <svg viewBox="0 0 14 14"><circle cx="7" cy="7" r="6" fill="none" stroke="#777" stroke-width="1.5"/><circle cx="7" cy="7" r="2.5" fill="#777"/></svg></span>
      </div>
      <div class="services__divider"></div>
      <div class="services__col services__col--right">
        <span class="service"><svg viewBox="0 0 14 14"><circle cx="7" cy="7" r="6" fill="none" stroke="#777" stroke-width="1.5"/><circle cx="7" cy="7" r="2.5" fill="#777"/></svg> Clinics</span>
        <span class="service"><svg viewBox="0 0 14 14"><circle cx="7" cy="7" r="6" fill="none" stroke="#777" stroke-width="1.5"/><circle cx="7" cy="7" r="2.5" fill="#777"/></svg> Private Training</span>
      </div>
    </div>
    <div class="band-back__rule band-back__rule--top"></div>
    <div class="band-back"></div>
    <div class="band-back__rule band-back__rule--bottom"></div>
    <div class="brand">
      <span class="brand__dot"></span>
      <span class="brand__name">RIVET</span>
    </div>
  </section>

  <section class="card card--front" aria-label="Card front">
    <div class="backdrop-circle" aria-hidden="true"></div>
    <h1 class="headline">Basketball Training program</h1>
    <div class="stripe"></div>
    <div class="band-front"></div>
    <div class="person">
      <p class="person__name">Marlo Quintrell</p>
      <p class="person__role">Boys &amp; Girls Basketball Coach</p>
    </div>
    <div class="contact-divider"></div>
    <ul class="contacts">
      <li><svg viewBox="0 0 18 18"><rect x="1" y="1" width="16" height="16" rx="2" fill="#fff"/><path d="M5 4c1 0 2 2 2 3s-1 1-1 1c.5 1.5 2 3 3.5 3.5 0 0 0-1 1-1s3 1 3 2-1 2-2 2C8 14 4 10 4 6c0-1 0-2 1-2z" fill="#111"/></svg>555-317-4826</li>
      <li><svg viewBox="0 0 18 18"><rect x="1" y="1" width="16" height="16" rx="2" fill="#fff"/><circle cx="9" cy="9" r="5" fill="none" stroke="#111" stroke-width="1.4"/><path d="M4 9h10M9 4c-2 3-2 7 0 10M9 4c2 3 2 7 0 10" fill="none" stroke="#111" stroke-width="1.1"/></svg>rivetbasketball.example</li>
      <li><svg viewBox="0 0 18 18"><rect x="1" y="1" width="16" height="16" rx="2" fill="#fff"/><rect x="4" y="5.5" width="10" height="7" fill="none" stroke="#111" stroke-width="1.4"/><path d="M4 5.5l5 4 5-4" fill="none" stroke="#111" stroke-width="1.4"/></svg>rivet.basketball@mailbox.example</li>
    </ul>
  </section>

</main>
</body>
</html>
```